Thornfield Marsh, LLC Website

We are a small law firm in need of a website that contains the following:
1. Attractive main page
2. About us/attorney info for three people: Leonard Thornfield (attorney), Brent Marsh (attorney), and Melinda Carrow (legal assistant). We have bio's ready to submit.
3. Blog/video page. We'd like to post blogs and videos to help drive traffic
4. Multidistrict Litigation and Class Actions page, where we post information regarding active MDLs and Class actions that we are doing intake on.
Updates

Can you also please use the color "gold" in the design and logo? Thanks.

Industry/Entity Type

Legal

Coding

Coded - Design and coding required

Number of Pages Required

1 page

Colors
0054AA
0677BA
7BADD7
CADEEF
E8F1F8

Requirements
Must have
• 1. Attractive main page 2. About us/attorney info for three people: Leonard Thornfield (attorney), Brent Marsh (attorney), and Melinda Carrow (legal assistant). We have bio's ready to submit. 3. Blog/video page. We'd like to post blogs and videos to help drive traffic 4. Multidistrict Litigation and Class Actions page, where we post information regarding active MDLs and Class actions that we are doing intake on.

```html
<!DOCTYPE html>
<html lang="en">
<head>
<meta charset="UTF-8">
<title>Thornfield Marsh, LLC — Justice Through Collective Action</title>
<link href="https://fonts.googleapis.com/css2?family=Inter:wght@400;500;600&family=Playfair+Display:wght@500;600;700&display=swap" rel="stylesheet">
<style>
:root{
  --navy:#142a8c;
  --blue:#0054aa;
  --blue-mid:#0677ba;
  --sky:#7badd7;
  --mist:#cadeef;
  --ice:#e8f1f8;
  --gold:#f5c518;
  --gold-soft:#fbe08a;
  --ink:#1c1f26;
  --muted:#5b6472;
  --teal-dark:#0f2c2f;
  --white:#ffffff;
  --serif:'Playfair Display', Georgia, serif;
  --sans:'Inter', Arial, sans-serif;
}
*{box-sizing:border-box;margin:0;padding:0}
html,body{width:1200px;height:3000px;overflow:hidden}
body{font-family:var(--sans);color:var(--ink);background:var(--white)}
.wrap{width:1060px;margin:0 auto}
.btn{display:inline-block;font:500 13px var(--sans);padding:9px 20px;border-radius:2px;text-decoration:none;white-space:nowrap;line-height:16px}
.btn-blue{background:var(--blue);color:var(--white)}
.btn-ghost{border:1px solid var(--white);color:var(--white)}
.btn-outline{border:1px solid var(--blue);color:var(--blue);background:var(--white)}
.btn-white{background:var(--white);color:var(--blue)}
.brand{display:flex;align-items:center;gap:8px;font:600 15px var(--sans);color:var(--navy)}
.brand-square{width:22px;height:22px;background:var(--gold)}
.ph{display:block}

/* nav */
.site-nav{height:60px;display:flex;align-items:center}
.site-nav .wrap{display:flex;align-items:center;justify-content:space-between}
.nav-links{display:flex;gap:28px;font-size:12.5px;color:var(--ink)}
.nav-links span.has-sub::after{content:" ›"}

/* hero */
.hero{position:relative;height:440px;overflow:hidden;text-align:center;color:var(--white)}
.hero .ph{position:absolute;inset:0;background:linear-gradient(180deg,#c9d4d6 0%,#a9b3b4 30%,#4a4845 55%,#1f1f1f 100%)}
.hero-inner{position:relative;padding-top:270px}
.hero h1{font:700 46px var(--serif);letter-spacing:.2px}
.hero p{font-size:17px;margin:8px 0 22px}
.hero .btns{display:flex;gap:14px;justify-content:center}
.hero .dots{position:absolute;bottom:6px;left:50%;transform:translateX(-50%);display:flex;gap:4px}
.hero .dots i{width:4px;height:4px;border-radius:50%;background:var(--white);opacity:.7}

/* trust */
.trust{height:120px;background:var(--ice);text-align:center;padding-top:16px}
.trust h4{font:500 14px var(--serif);margin-bottom:16px}
.badges{display:flex;justify-content:center;gap:56px;align-items:center}
.badge{background:#3b3f47;height:44px}
.badge.shield{width:40px;border-radius:4px 4px 20px 20px}
.badge.wide{width:150px;background:#2d3138}
.badge.thin{width:110px;height:30px;background:#b7bcc4}
.badge.word{width:96px;height:30px;background:#1c1f26}

/* about */
.about{height:380px;display:flex;overflow:hidden}
.about .ph{width:560px;height:100%;background:linear-gradient(180deg,#ffffff 0%,#f3efe2 30%,#8a8a8a 70%,#3a3a3a 100%)}
.about-copy{padding:36px 0 0 30px;width:610px}
.eyebrow{font:500 13px var(--serif)}
.about h2{font:700 28px var(--serif);color:var(--navy);margin:10px 0 14px;white-space:nowrap}
.about p{font-size:11px;color:var(--muted);line-height:1.45;max-width:520px}
.tags{display:flex;margin:20px 0 34px;font:500 14px var(--serif)}
.tags span{padding:0 12px;border-left:1px solid var(--blue)}
.tags span:first-child{padding-left:0;border:0}
.team{display:flex;gap:40px;margin-bottom:28px}
.team b{display:block;font:500 15px var(--serif);color:var(--blue)}
.team small{font-size:10px;color:var(--muted)}

/* practice */
.practice{height:600px;background:var(--blue);color:var(--white);text-align:center;padding-top:30px}
.practice h2{font:600 26px var(--serif);margin-bottom:26px;line-height:35px}
.pa-grid{width:922px;margin:0 auto;display:grid;grid-template-columns:repeat(3,290px);column-gap:26px;row-gap:20px;text-align:left}
.pa-card{height:200px}
.pa-card .ph{height:134px}
.pa-card h3{font:500 13px var(--sans);margin:9px 0 5px}
.pa-card p{font-size:10px;line-height:1.3;max-width:240px}
.pa-card.active{background:var(--mist);color:var(--navy)}
.pa-card.active h3,.pa-card.active p{padding:0 8px}
.practice .btn{margin-top:26px}

/* insights */
.insights{height:540px;padding-top:40px}
.ins-top{display:flex;gap:44px;margin-bottom:36px}
.featured{width:460px;background:var(--blue);color:var(--white);position:relative}
.featured .ph{height:180px;background:radial-gradient(ellipse at 50% 50%,#3f8fc7 0%,#123a5c 40%,#02060c 75%)}
.featured .cap{padding:12px 10px}
.featured h3{font:500 13px var(--sans)}
.featured small{font-size:9px}
.pill{position:absolute;top:8px;right:8px;background:var(--gold);color:var(--ink);font-size:8px;padding:3px 7px;border-radius:10px}
.ins-copy{padding-top:6px}
.ins-copy h2{font:600 24px var(--serif);color:var(--navy)}
.ins-copy p{font:400 17px var(--serif);color:var(--muted);max-width:420px;margin:12px 0 18px;line-height:1.4}
.ins-row{display:grid;grid-template-columns:repeat(3,330px);gap:35px}
.post{position:relative}
.post .ph{height:150px}
.post h4{font:500 13px var(--sans);margin:12px 0 8px;line-height:1.35}
.post small{font-size:9px;color:var(--muted)}

/* contact */
.contact{height:420px;background:linear-gradient(160deg,#164348 0%,#0f2c2f 45%,#0a1e21 100%);position:relative;overflow:hidden}
.contact .ph{position:absolute;left:120px;top:0;width:420px;height:100%;background:radial-gradient(ellipse at 50% 70%,rgba(60,110,115,.55) 0%,rgba(15,44,47,0) 70%)}
.contact .wrap{position:relative;display:flex;justify-content:space-between;padding-top:28px}
.contact-left{width:460px;color:var(--white);padding-top:56px}
.contact-left h2{font:600 22px var(--serif);color:var(--gold);line-height:1.3}
.contact-left .lead{font:500 13px var(--sans);margin:8px 0 30px;padding-bottom:30px;border-bottom:1px solid rgba(255,255,255,.35)}
.contact-left h3{font:500 18px var(--sans);margin-bottom:10px}
.contact-left p{font-size:12px;line-height:1.8}
.form{width:470px;background:var(--white);padding:24px 46px 22px}
.form h4{font:500 12px var(--sans);color:var(--blue);margin-bottom:14px}
.row{display:flex;gap:8px;margin-bottom:8px}
.field{flex:1;height:24px;background:var(--ice);font-size:8.5px;color:var(--muted);padding:7px 8px;display:flex;justify-content:space-between}
.field.msg{height:100px}
.consent{display:flex;gap:6px;font-size:8px;color:var(--muted);margin:10px 0 6px;line-height:1.4}
.tick{width:9px;height:9px;background:var(--blue-mid);flex:none;margin-top:1px}
.legal{font-size:8px;color:var(--muted);text-align:center;margin-bottom:14px}
.legal a,.agree a{color:var(--blue);text-decoration:none}
.form .submit{display:block;width:150px;margin:0 auto;text-align:center;padding:9px 0}

/* newsletter */
.newsletter{height:150px;background:var(--ice);padding-top:30px}
.newsletter h2{font:500 22px var(--serif);color:var(--navy);margin-bottom:24px}
.sub{display:flex}
.sub .field{flex:none;width:316px;height:34px;background:var(--white);font-size:11px;color:var(--ink);padding:10px 10px}
.sub .btn{padding:9px 24px}
.agree{display:flex;gap:6px;font-size:8px;margin-top:10px;align-items:center}

/* footer */
.footer{height:290px;padding-top:30px}
.foot-top{display:flex;align-items:center;justify-content:space-between;padding-bottom:22px;border-bottom:1px solid #cfd3d8}
.foot-top .badges{gap:60px}
.foot-cols{display:flex;gap:56px;padding-top:22px;font-size:11px}
.foot-cols h5{font:500 12px var(--sans);margin-bottom:8px}
.foot-cols li{list-style:none;line-height:2;color:#3c4350}
.foot-cols .ci li{display:flex;gap:8px;align-items:center}
.socials{display:flex;gap:9px}
.socials i{width:11px;height:11px;border-radius:50%;background:var(--ink)}
.copy{border-top:1px solid #cfd3d8;margin-top:20px;padding-top:8px;text-align:center;font-size:8.5px;color:var(--muted)}
</style>
</head>
<body>

<header class="site-nav">
  <div class="wrap">
    <div class="brand"><span class="brand-square"></span>Thornfield Marsh, LLC</div>
    <nav class="nav-links">
      <span>Home</span><span>About</span><span>Attorneys</span><span>MDLs &amp; Class Actions</span>
      <span class="has-sub">Practice Area</span><span class="has-sub">Resources</span>
    </nav>
    <a class="btn btn-blue" href="#contact">Contact us</a>
  </div>
</header>

<section class="hero">
  <div class="ph" role="img" aria-label="Upward view of a tall stone courthouse tower with columns"></div>
  <div class="hero-inner">
    <h1>Justice Through Collective Action</h1>
    <p>Your Trusted Advocates in Multidistrict Litigation</p>
    <div class="btns"><a class="btn btn-blue" href="#contact">Free Case Evaluation</a><a class="btn btn-ghost" href="#">View MDL Cases</a></div>
  </div>
  <div class="dots"><i></i><i></i><i></i></div>
</section>

<section class="trust">
  <h4>Trusted By :</h4>
  <div class="badges">
    <span class="badge shield"></span><span class="badge wide"></span><span class="badge thin"></span><span class="badge word"></span>
  </div>
</section>

<section class="about">
  <div class="ph" role="img" aria-label="Portrait of the three firm members in business suits"></div>
  <div class="about-copy">
    <div class="eyebrow">About Thornfield Marsh LLP</div>
    <h2>Collective Strength. Individual Justice.</h2>
    <p>Thornfield Marsh LLC is a multi-service law firm located in downtown Bayport, Alabama. Our Bayport business litigation lawyers are licensed to practice law in the following Gulf Coast states: Alabama and Florida.</p>
    <div class="tags"><span>Insurance Claims</span><span>Wage Disputes</span><span>Medicare Fraud</span><span>Civil Litigation</span></div>
    <div class="team">
      <div><b>Leonard Thornfield</b><small>Attorney</small></div>
      <div><b>Brent Marsh</b><small>Attorney</small></div>
      <div><b>Melinda Carrow</b><small>Legal Assistant</small></div>
    </div>
    <a class="btn btn-outline" href="#">Learn more about us</a>
  </div>
</section>

<section class="practice">
  <h2>Practice Areas</h2>
  <div class="pa-grid">
    <div class="pa-card active"><div class="ph" role="img" aria-label="Damaged cars after a collision" style="background:linear-gradient(160deg,#4d5a48,#7d848a 50%,#2e3338)"></div><h3>Auto Accident &amp; Insurance Claims</h3><p>Resolving disputes for policyholders against unfair claim denials.</p></div>
    <div class="pa-card"><div class="ph" role="img" aria-label="Worker in orange safety vest and hard hat in a factory" style="background:linear-gradient(160deg,#6a7078,#d9772b 50%,#3b4048)"></div><h3>Employment Law</h3><p>Protecting workers' rights in wage disputes, discrimination, and OSHA cases.</p></div>
    <div class="pa-card"><div class="ph" role="img" aria-label="Gavel, pen and clipboard with documents" style="background:linear-gradient(160deg,#5a3a2a,#f2f2f2 45%,#d8d8d8)"></div><h3>General Litigation</h3><p>Resolving business conflicts, from contracts to fiduciary disputes.</p></div>
    <div class="pa-card"><div class="ph" role="img" aria-label="Hands reviewing papers next to a calculator" style="background:linear-gradient(160deg,#f3d3b0,#c88a5c 55%,#3a2a22)"></div><h3>Collections</h3><p>Our firm represents businesses who seek to collect from other businesses and from consumers.</p></div>
    <div class="pa-card"><div class="ph" role="img" aria-label="Gavel, pills and banknotes on a white surface" style="background:linear-gradient(160deg,#f6f6f2,#d9dccf 55%,#8a6a4a)"></div><h3>Medicare Fraud (False Claims Act)</h3><p>Whistleblower litigation to expose healthcare fraud.</p></div>
    <div class="pa-card"><div class="ph" role="img" aria-label="Two people shaking hands across an office table" style="background:linear-gradient(160deg,#dfe6ea,#8ea7bd 55%,#4a6a8a)"></div><h3>Mediation &amp; Arbitration</h3><p>Alternative dispute resolution led by certified neutrals.</p></div>
  </div>
  <a class="btn btn-white" href="#contact">Free Case Evaluation</a>
</section>

<section class="insights">
  <div class="wrap">
    <div class="ins-top">
      <article class="featured">
        <span class="pill">Mass Tort Lawsuit</span>
        <div class="ph" role="img" aria-label="X-ray scan of a human torso with a medical device"></div>
        <div class="cap"><h3>5 Signs Your Medical Device Qualifies for a Mass Tort Lawsuit.</h3><small>Updated: 5 Apr 2025</small></div>
      </article>
      <div class="ins-copy">
        <h2>Insights</h2>
        <p>Explore our latest articles, MDL rulings, and practical guides to navigate complex litigation.</p>
        <a class="btn btn-blue" href="#">View all</a>
      </div>
    </div>
    <div class="ins-row">
      <article class="post"><span class="pill">Brushfield Bottle</span><div class="ph" role="img" aria-label="Brown glass bottle standing in green grass" style="background:linear-gradient(160deg,#2f4a1c,#5d7a2a 50%,#1a2a10)"></div><h4>2024 Brushfield Weed Killer Litigation: Latest Updates for Victims</h4><small>Updated: 2 Mar 2025</small></article>
      <article class="post"><span class="pill">Camp Redfield water</span><div class="ph" role="img" aria-label="Service member in uniform holding a child beside a woman outdoors" style="background:linear-gradient(160deg,#c9b79a,#8f8a6a 50%,#d8cbb8)"></div><h4>Camp Redfield Water Contamination: How to File a Claim Before 2025</h4><small>Updated: 10 Feb 2025</small></article>
      <article class="post"><span class="pill">Class Action vs MDL</span><div class="ph" role="img" aria-label="Aerial view of apartment buildings and courtyards" style="background:linear-gradient(160deg,#6f7a70,#b9bcb4 50%,#3e4a42)"></div><h4>Class Action vs. MDL: Which Is Right for Your Case?</h4><small>Updated: 1 Jan 2025</small></article>
    </div>
  </div>
</section>

<section class="contact" id="contact">
  <div class="ph" role="img" aria-label="Dim silhouette of scales of justice"></div>
  <div class="wrap">
    <div class="contact-left">
      <h2>Should you or your business have a<br>legal concern?</h2>
      <p class="lead">we would be honored to provide you with a legal consultation.</p>
      <h3>Contact Us</h3>
      <p>214 Harbor Row, Bayport, AL 36690<br>Phone - (251) 555-0142<br>Fax - (251) 555-0143</p>
    </div>
    <form class="form">
      <h4>Fill out the contact form to schedule your consultation.</h4>
      <div class="row"><div class="field">First Name</div><div class="field">Last Name</div></div>
      <div class="row"><div class="field">Phone Number</div><div class="field">Email</div></div>
      <div class="row"><div class="field">Case Type <span>⌄</span></div></div>
      <div class="row"><div class="field msg">Message...</div></div>
      <div class="consent"><span class="tick"></span><span>I hereby expressly consent to receive automated communications including calls, texts, emails, and/or prerecorded messages.</span></div>
      <p class="legal">By submitting this form, you agree to our Terms &amp; acknowledge our <a href="#">Privacy Policy</a>.</p>
      <a class="btn btn-blue submit" href="#">Submit Request</a>
    </form>
  </div>
</section>

<section class="newsletter">
  <div class="wrap">
    <h2>Subscribe to our firm newsletter !</h2>
    <div class="sub"><div class="field">Email</div><a class="btn btn-blue" href="#">Subscribe Now</a></div>
    <div class="agree"><span class="tick"></span>I agree to the <a href="#">Privacy Policy.</a></div>
  </div>
</section>

<footer class="footer">
  <div class="wrap">
    <div class="foot-top">
      <div class="brand"><span class="brand-square"></span>Thornfield Marsh, LLC</div>
      <div class="badges"><span class="badge shield"></span><span class="badge wide"></span><span class="badge thin"></span><span class="badge word"></span></div>
    </div>
    <div class="foot-cols">
      <div><h5>Quick Links</h5><ul><li>Home</li><li>About Our Firm</li><li>MDL &amp; Class Actions</li><li>Attorney Profiles</li><li>Contact Us</li></ul></div>
      <div><h5>Resources</h5><ul><li>Legal Updates</li><li>Blogs</li><li>FAQ's</li></ul></div>
      <div><h5>Practice Areas</h5><ul><li>Auto Accident &amp; Insurance Claims</li><li>Employment Law</li><li>General Litigation</li><li>Collections</li><li>Medical Fraud</li><li>Mediation &amp; Arbitration</li></ul></div>
      <div class="ci"><h5>Contact Info</h5><ul>
        <li><svg width="11" height="11" viewBox="0 0 24 24" fill="none" stroke="#1c1f26" stroke-width="2"><path d="M12 22s7-7 7-12a7 7 0 0 0-14 0c0 5 7 12 7 12z"/><circle cx="12" cy="10" r="2.5"/></svg>214 Harbor Row, Bayport, AL 36690</li>
        <li><svg width="11" height="11" viewBox="0 0 24 24" fill="none" stroke="#1c1f26" stroke-width="2"><path d="M5 3h4l2 5-3 2a11 11 0 0 0 6 6l2-3 5 2v4a2 2 0 0 1-2 2A18 18 0 0 1 3 5a2 2 0 0 1 2-2z"/></svg>(251) 555-0142</li>
        <li><svg width="11" height="11" viewBox="0 0 24 24" fill="none" stroke="#1c1f26" stroke-width="2"><rect x="3" y="5" width="18" height="14"/><path d="M3 6l9 7 9-7"/></svg>info@thornfieldmarsh.com</li>
      </ul></div>
      <div><h5>Socials</h5><div class="socials"><i></i><i></i><i></i><i></i><i></i></div></div>
    </div>
    <p class="copy">Copyright © 2025 Thornfield Marsh LLC. All Rights Reserved.</p>
  </div>
</footer>

</body>
</html>
```